Cover for Inspirational Daily Journal

This is the cover for a daily journal that will focus on inspirational content for black women. The cover should have a picture or silhouette of a black woman with a crown. The title is: "Grace in Bloom: A Year of Bright Mornings." The back won't have any words. Also the journal will be published on Pagewick.

```html
<!DOCTYPE html>
<html lang="en">
<head>
<meta charset="utf-8">
<title>Grace in Bloom – Journal Cover</title>
<link href="https://fonts.googleapis.com/css2?family=Bebas+Neue&family=Great+Vibes&family=Montserrat:wght@600;700&display=swap" rel="stylesheet">
<style>
  :root {
    --stage: #e1e2e4;
    --cover-grey: #939496;
    --silhouette: #000000;
    --gold: #fbb61e;
    --gold-deep: #e59a12;
    --white: #ffffff;
    --gem: #2fb8dc;
  }
  html, body {
    margin: 0;
    width: 1200px;
    height: 1200px;
    overflow: hidden;
    background: var(--stage);
  }
  .book-cover {
    position: absolute;
    left: 360px;
    top: 240px;
    width: 480px;
    height: 720px;
    background: var(--cover-grey);
    overflow: hidden;
  }
  .portrait-silhouette {
    position: absolute;
    left: 0;
    top: 0;
    width: 480px;
    height: 720px;
  }
  .crown-art {
    position: absolute;
    left: 8px;
    top: 62px;
    width: 254px;
    height: 200px;
    border-radius: 40% 40% 50% 50% / 60% 60% 30% 30%;
    background: linear-gradient(180deg, #fff3b8 0%, var(--gold) 45%, var(--gold-deep) 100%);
  }
  .title {
    margin: 0;
    font-weight: normal;
  }
  .title-main {
    position: absolute;
    left: 40px;
    top: 212px;
    font-family: "Bebas Neue", sans-serif;
    font-size: 176px;
    line-height: 1;
    color: var(--white);
    letter-spacing: 0.01em;
  }
  .title-joiner {
    position: absolute;
    left: 372px;
    top: 262px;
    font-family: "Great Vibes", cursive;
    font-size: 64px;
    line-height: 1;
    color: var(--white);
  }
  .title-accent {
    position: absolute;
    left: 34px;
    top: 366px;
    font-family: "Bebas Neue", sans-serif;
    font-size: 160px;
    line-height: 1;
    color: var(--gold);
    letter-spacing: 0.01em;
  }
  .subtitle {
    position: absolute;
    left: 15px;
    width: 400px;
    text-align: center;
    font-family: "Montserrat", sans-serif;
    color: var(--white);
    margin: 0;
  }
  .subtitle-lead {
    top: 522px;
    font-size: 25px;
    font-weight: 600;
    letter-spacing: 0.45em;
    text-indent: 0.45em;
  }
  .subtitle-main {
    top: 554px;
    font-size: 31px;
    font-weight: 700;
    letter-spacing: 0.1em;
    text-indent: 0.1em;
  }
  .author-name {
    position: absolute;
    left: 57px;
    width: 300px;
    top: 676px;
    text-align: center;
    font-family: "Montserrat", sans-serif;
    font-weight: 700;
    font-size: 16px;
    letter-spacing: 0.12em;
    color: var(--white);
    margin: 0;
  }
</style>
</head>
<body>
  <main class="book-cover">
    <svg class="portrait-silhouette" viewBox="0 0 480 720" role="img" aria-label="Silhouette of a Black woman in profile">
      <path fill="var(--silhouette)" d="M0 100 Q0 60 70 60 L290 60 Q457 60 457 260 L457 560 Q457 625 395 625 L272 625 L270 720 L0 720 Z"/>
    </svg>
    <div class="crown-art" role="img" aria-label="Gold jewelled crown with blue gems"></div>

    <h1 class="title">
      <span class="title-main">GRACE</span>
      <span class="title-joiner">in</span>
      <span class="title-accent">BLOOM</span>
    </h1>
    <p class="subtitle subtitle-lead">A YEAR OF</p>
    <p class="subtitle subtitle-main">BRIGHT MORNINGS</p>

    <p class="author-name">AUTHOR NAME</p>
  </main>
</body>
</html>
```